Horse Brush Package design -

I need a design for a box - required for a rubber horse brush used for grooming and removing excess hair. The Brand is 'Maple Ridge Equestrian' and we develop top quality horse products. The design should be classy and professional

Box size is 21.5cm Length * 2cm high * 5 cm wide
Photo of logo and brush attached.
Box needs to have logo and description on front
Barcode on back.
Additional designs and photos can be added as you see fit.

"Horse Deshedding & Grooming Brush"
Brush away excess coat and dander
Gently remove dirt and mud
Soft, flexible design to gently groom around legs, ears and face.
Used when washing gives a deep clean to remove dirt
Gentle massage for increasing circulation
Durable, gentle, and kind to the horse

Target Market(s)

Horse Owners

Requirements
Must have
• Logo on the front, space for barcode on the back
Nice to have
• A nice horse photo would be suitable

```html
<!DOCTYPE html>
<html lang="en">
<head>
<meta charset="utf-8">
<title>Maple Ridge Equestrian – Deshedding Brush Box Dieline</title>
<link rel="stylesheet" href="https://fonts.googleapis.com/css2?family=Teko:wght@600&family=Montserrat:wght@500;600;700&display=swap">
<style>
  :root{
    --gold:#ce9530;
    --ink:#333333;
    --cut:#e5141b;
    --paper:#ffffff;
    --soft:#f1f1f1;
    --rubber-dark:#161616;
    --rubber-mid:#3c3c3c;
  }
  *{box-sizing:border-box;margin:0;padding:0}
  html,body{width:1200px;height:1200px;overflow:hidden;background:var(--paper)}
  body{position:relative;font-family:"Montserrat",sans-serif;color:var(--ink)}
  .dieline{position:absolute;left:0;top:0;width:1200px;height:1200px}
  .abs{position:absolute}
  .brand{font-family:"Montserrat",sans-serif;font-weight:600;color:var(--gold);white-space:nowrap;letter-spacing:.5px}
  .brand--light{color:#fff}
  .headline{font-family:"Teko",sans-serif;font-weight:600;line-height:.9;letter-spacing:.5px;white-space:nowrap}
  .headline .gold{color:var(--gold)}
  .tagbar{background:linear-gradient(90deg,#222,#555);color:#fff;font-weight:700;font-size:8.6px;border-radius:4px;padding:3px 8px;white-space:nowrap;text-align:center}
  .brush-photo{border-radius:14px;background:linear-gradient(180deg,var(--rubber-mid) 0%,var(--rubber-dark) 55%,#2a2a2a 100%);box-shadow:0 3px 6px rgba(0,0,0,.25)}
  .horse-photo{background:linear-gradient(90deg,#ffffff 0%,#d9d9d9 18%,#5a5a5a 45%,#1e1e1e 70%,#3a3a3a 100%)}
  .side-brand{font-size:11px;transform-origin:center;line-height:1.15}
  .bullets{list-style:none;font-size:6.6px;font-weight:600;line-height:14.7px;white-space:nowrap}
  .bullets li{display:flex;align-items:center;gap:6px}
  .tick{width:7px;height:7px;border:1px solid var(--gold);display:inline-flex;align-items:center;justify-content:center;flex:none}
  .tile{width:84px;height:75px;border:1px solid var(--gold);display:flex;flex-direction:column}
  .tile__art{flex:1;background:linear-gradient(180deg,#fbfbfb 0%,#ececec 100%)}
  .tile__label{height:21px;background:var(--gold);color:#fff;font-size:6px;font-weight:700;display:flex;align-items:center;justify-content:center;text-transform:uppercase;white-space:nowrap}
  .maker{width:170px;text-align:center;font-size:8.5px;font-weight:500}
  .maker__name{color:var(--gold);font-weight:700;font-size:11.5px;margin:2px 0 4px}
  .handle{display:flex;align-items:center;justify-content:center;gap:4px;margin-bottom:5px}
  .handle i{width:10px;height:10px;background:var(--gold);border-radius:2px;display:inline-block}
  .barcode-space{width:137px;height:62px;background:var(--soft)}
  .feature{display:flex;align-items:center;gap:9px;color:#fff;font-weight:700;font-size:10.5px;line-height:11px;text-transform:uppercase;white-space:nowrap}
  .feature__icon{width:44px;height:44px;border-radius:50%;background:#fff;border:2px solid #fff;box-shadow:inset 0 0 0 2px var(--gold);display:flex;align-items:center;justify-content:center}
</style>
</head>
<body>

<svg class="dieline" viewBox="0 0 1200 1200" aria-hidden="true">
  <g fill="var(--gold)">
    <polygon points="173,301 1027,301 1037,328 163,328"/>
    <rect x="163" y="532" width="874" height="81"/>
    <rect x="163" y="816" width="874" height="82"/>
  </g>
  <g fill="none" stroke="var(--cut)" stroke-width="1.2">
    <polygon points="173,301 1027,301 1037,328 163,328"/>
    <rect x="163" y="328" width="874" height="570"/>
    <line x1="163" y1="532" x2="1037" y2="532"/>
    <line x1="163" y1="613" x2="1037" y2="613"/>
    <line x1="163" y1="816" x2="1037" y2="816"/>
    <path d="M163,328 H68 Q59,328 59,337 V523 Q59,532 68,532 H163"/>
    <line x1="82" y1="328" x2="82" y2="532"/>
    <path d="M1037,328 H1132 Q1141,328 1141,337 V523 Q1141,532 1132,532 H1037"/>
    <line x1="1118" y1="328" x2="1118" y2="532"/>
    <path d="M163,533 L143,538 H100 V607 H143 L163,612"/>
    <path d="M1037,533 L1057,538 H1100 V607 H1057 L1037,612"/>
    <path d="M163,817 L143,822 H100 V892 H143 L163,897"/>
    <path d="M1037,817 L1057,822 H1100 V892 H1057 L1037,897"/>
  </g>
  <line x1="820" y1="635" x2="820" y2="794" stroke="var(--gold)" stroke-width="2"/>
</svg>

<!-- end flaps -->
<div class="abs brand side-brand" style="left:67px;top:410px;width:110px;text-align:center;transform:rotate(-90deg)">MAPLE RIDGE<br><span style="font-size:7px">EQUESTRIAN</span></div>
<div class="abs brand side-brand" style="left:1023px;top:410px;width:110px;text-align:center;transform:rotate(90deg)">MAPLE RIDGE<br><span style="font-size:7px">EQUESTRIAN</span></div>

<!-- front panel -->
<div class="abs brand" style="left:184px;top:364px;font-size:17px;line-height:1">MAPLE RIDGE<br><span style="font-size:10px">EQUESTRIAN</span></div>
<div class="abs headline" style="left:184px;top:424px;font-size:34px">
  <span class="gold">HORSE DESHEDDING</span><br>&amp; GROOMING BRUSH
</div>
<div class="abs tagbar" style="left:184px;top:482px;width:218px">BRUSH AWAY EXCESS COAT AND DANDER</div>

<div class="abs brush-photo" role="img" aria-label="Product photo: black rubber grooming brush, handle side" style="left:430px;top:372px;width:258px;height:64px;transform:rotate(-6deg)"></div>
<div class="abs brush-photo" role="img" aria-label="Product photo: black rubber grooming brush, textured nub side" style="left:500px;top:444px;width:258px;height:64px;transform:rotate(-6deg)"></div>

<div class="abs horse-photo" role="img" aria-label="Black and white photo of a black horse with a flowing mane" style="left:795px;top:328px;width:242px;height:204px"></div>
<svg class="abs" style="left:976px;top:351px" width="40" height="62" viewBox="0 0 40 62" aria-hidden="true">
  <rect x="8" y="22" width="24" height="38" fill="var(--gold)"/>
  <polygon points="20,0 38,10 38,30 20,40 2,30 2,10" fill="#3a3a3a" stroke="#bdbdbd" stroke-width="1.5"/>
</svg>

<!-- top side band -->
<div class="abs brand brand--light" style="left:184px;top:558px;font-size:16px;line-height:1">MAPLE RIDGE<br><span style="font-size:9.5px">EQUESTRIAN</span></div>
<div class="abs headline" style="right:165px;top:557px;font-size:33px;color:#fff">HORSE DESHEDDING &amp; GROOMING BRUSH</div>

<!-- back panel -->
<div class="abs headline" style="left:184px;top:632px;font-size:31px">
  <span class="gold">HORSE DESHEDDING</span><br>&amp; GROOMING BRUSH
</div>
<ul class="abs bullets" style="left:184px;top:692px">
  <li><span class="tick"><svg width="5" height="5" viewBox="0 0 5 5"><path d="M0.5,2.5 L2,4 L4.5,1" fill="none" stroke="var(--gold)" stroke-width="1"/></svg></span>Brush away excess coat and dander.</li>
  <li><span class="tick"><svg width="5" height="5" viewBox="0 0 5 5"><path d="M0.5,2.5 L2,4 L4.5,1" fill="none" stroke="var(--gold)" stroke-width="1"/></svg></span>Gently remove dirt and mud.</li>
  <li><span class="tick"><svg width="5" height="5" viewBox="0 0 5 5"><path d="M0.5,2.5 L2,4 L4.5,1" fill="none" stroke="var(--gold)" stroke-width="1"/></svg></span>Soft, flexible design to gently groom around legs, ears and face.</li>
  <li><span class="tick"><svg width="5" height="5" viewBox="0 0 5 5"><path d="M0.5,2.5 L2,4 L4.5,1" fill="none" stroke="var(--gold)" stroke-width="1"/></svg></span>Used when washing gives a deep clean to remove dirt.</li>
  <li><span class="tick"><svg width="5" height="5" viewBox="0 0 5 5"><path d="M0.5,2.5 L2,4 L4.5,1" fill="none" stroke="var(--gold)" stroke-width="1"/></svg></span>Gentle massage for increasing circulation.</li>
  <li><span class="tick"><svg width="5" height="5" viewBox="0 0 5 5"><path d="M0.5,2.5 L2,4 L4.5,1" fill="none" stroke="var(--gold)" stroke-width="1"/></svg></span>Durable, gentle, and kind to the horse.</li>
</ul>

<div class="abs tile" style="left:432px;top:633px"><div class="tile__art" role="img" aria-label="Line illustration: brushing a horse's body"></div><div class="tile__label">Grooms the body</div></div>
<div class="abs tile" style="left:527px;top:633px"><div class="tile__art" role="img" aria-label="Line illustration: brushing a horse's face"></div><div class="tile__label">Grooms the face</div></div>
<div class="abs tile" style="left:622px;top:633px"><div class="tile__art" role="img" aria-label="Line illustration: brushing a horse's legs"></div><div class="tile__label">Grooms the legs</div></div>
<div class="abs tile" style="left:716px;top:633px"><div class="tile__art" role="img" aria-label="Line illustration: shedding loose coat"></div><div class="tile__label">Sheds the coat</div></div>
<div class="abs tile" style="left:432px;top:720px"><div class="tile__art" role="img" aria-label="Line illustration: cleaning a hoof wall"></div><div class="tile__label">Cleans hoof walls</div></div>
<div class="abs tile" style="left:527px;top:720px"><div class="tile__art" role="img" aria-label="Line illustration: lathering shampoo"></div><div class="tile__label">Lathers shampoo</div></div>
<div class="abs tile" style="left:622px;top:720px"><div class="tile__art" role="img" aria-label="Line illustration: shining the coat"></div><div class="tile__label">Shines the coat</div></div>
<div class="abs tile" style="left:716px;top:720px"><div class="tile__art" role="img" aria-label="Line illustration: massaging muscles"></div><div class="tile__label">Massages muscles</div></div>

<div class="abs maker" style="left:848px;top:633px">
  <div>Manufacture by:</div>
  <div class="maker__name">Maple Ridge Equestrian</div>
  <div class="handle"><i></i>@MapleRidgeEquestrian</div>
  <div class="handle"><i></i>@MapleRidgeEquestrian</div>
  <svg width="20" height="20" viewBox="0 0 20 20" aria-hidden="true"><g fill="none" stroke="#333" stroke-width="2" stroke-linejoin="round"><path d="M8,3 L12,3 L15,8"/><path d="M16,12 L14,16 L8,16"/><path d="M5,15 L3,11 L6,6"/></g><g fill="#333"><path d="M13,6 L17,7 L16,10 Z"/><path d="M9,14 L6,16 L9,18 Z"/><path d="M4,8 L6,5 L8,8 Z"/></g></svg>
</div>
<div class="abs barcode-space" style="left:866px;top:721px"></div>
<div class="abs" style="left:848px;top:786px;width:170px;text-align:center;font-size:9px;font-weight:500">Made in China</div>

<!-- bottom band features -->
<div class="abs feature" style="left:343px;top:835px">
  <div class="feature__icon"><svg width="24" height="10"><rect width="24" height="9" rx="1" fill="var(--gold)"/></svg></div>
  <div>Bristle &amp;<br>Blade free<br>design</div>
</div>
<div class="abs feature" style="left:484px;top:835px">
  <div class="feature__icon"><svg width="22" height="22" viewBox="0 0 22 22"><g fill="none" stroke="var(--gold)" stroke-width="2.4" stroke-linecap="round"><path d="M9,13 L13,9"/><path d="M10,6 L12,4 A4,4 0 0 1 18,10 L16,12"/><path d="M12,16 L10,18 A4,4 0 0 1 4,12 L6,10"/></g></svg></div>
  <div>Durable,<br>gentle</div>
</div>
<div class="abs feature" style="left:612px;top:835px">
  <div class="feature__icon"><svg width="20" height="22" viewBox="0 0 20 22"><path d="M10,1 L18,4 V11 C18,16 14,19 10,21 C6,19 2,16 2,11 V4 Z" fill="var(--gold)"/><path d="M6,11 L9,14 L14,8" fill="none" stroke="#fff" stroke-width="2"/></svg></div>
  <div>Flexible &amp;<br>safe</div>
</div>
<div class="abs feature" style="left:746px;top:835px">
  <div class="feature__icon"><svg width="24" height="24" viewBox="0 0 24 24" fill="var(--gold)"><path d="M14,6 L16,12 L22,14 L16,16 L14,22 L12,16 L6,14 L12,12 Z"/><path d="M6,2 L7,5 L10,6 L7,7 L6,10 L5,7 L2,6 L5,5 Z"/></svg></div>
  <div>Clean &amp;<br>sanitary</div>
</div>

</body>
</html>
```